Real Estate agent needs flyer/folder to contain bio and overview of services

I'm including files of the layout of the small folder. The folder is 6 1/2 across and 9 1/2 inches long. It will have a front & back cover and then writing on the 2 inside pages.

I am sending a few files to incorporate into the flyer, 1 new logo to use and 2 files which are coloring ideas.

```html
<!DOCTYPE html>
<html lang="en">
<head>
<meta charset="utf-8">
<title>Realtor Folder – Inside Spread</title>
<link rel="stylesheet" href="https://fonts.googleapis.com/css2?family=Roboto+Condensed:wght@400;700&family=Zilla+Slab:wght@300;400&display=swap">
<style>
  :root{
    --navy:#141b2c;
    --navy-deep:#0d1322;
    --navy-soft:#26324a;
    --yellow:#e6e23a;
    --red:#cc252b;
    --ink:#1b1b1b;
    --body-light:#c9ccd4;
    --rule:#cfc98a;
  }
  *{box-sizing:border-box;margin:0;padding:0}
  html,body{width:1200px;height:849px;overflow:hidden;background:#fff}
  .canvas{position:relative;width:1200px;height:849px;background:#fff}
  .spread-art{position:absolute;left:0;top:0}
  .copy{position:absolute;font-family:"Zilla Slab",Georgia,serif;font-weight:300;color:var(--body-light);font-size:9.7px;line-height:12.1px}
  .copy p{margin:0 0 10px}
  .title-light{font-family:"Roboto Condensed",Arial,sans-serif;font-weight:400;color:var(--yellow);font-size:17px;line-height:20px;margin-bottom:2px}
  .section-title{display:flex;align-items:flex-end;gap:5px;font-family:"Roboto Condensed",Arial,sans-serif;font-weight:700;color:var(--yellow);font-size:18px;line-height:18px;margin-bottom:15px;white-space:nowrap}
  .section-title::after{content:"";flex:1;border-bottom:1px dotted var(--rule);margin-bottom:3px}
  .intro{left:271px;top:120px;width:270px}
  .tenet{left:271px;top:334px;width:270px}
  .services{left:174px;top:581px;width:365px;color:var(--ink);font-size:12.4px;line-height:13.4px}
  .services p{margin:0 0 10px}
  .services h2{font-family:"Roboto Condensed",Arial,sans-serif;font-weight:400;font-size:26px;line-height:28px;margin-bottom:8px;color:var(--ink)}
  .selling{left:620px;top:138px;width:190px}
  .buying{left:826px;top:138px;width:206px}
  .testimonials{left:620px;top:522px;width:410px}
  .testimonial-cols{display:flex;gap:20px}
  .testimonial-cols > div{width:186px}
  .testimonial-cols > div + div{width:206px}
</style>
</head>
<body>
<div class="canvas">
  <svg class="spread-art" width="1200" height="849" viewBox="0 0 1200 849" aria-hidden="false">
    <defs>
      <clipPath id="cover-curve">
        <path d="M113 80 Q52 426 113 772 L587 772 L587 80 Z"/>
      </clipPath>
      <radialGradient id="keys-photo" cx="0.35" cy="0.85" r="0.8">
        <stop offset="0" stop-color="#6b4a45"/>
        <stop offset="0.35" stop-color="#2c3550"/>
        <stop offset="1" stop-color="#111829"/>
      </radialGradient>
      <radialGradient id="right-glow" cx="0" cy="0.75" r="0.6">
        <stop offset="0" stop-color="#2a3a55"/>
        <stop offset="1" stop-color="#121a2b"/>
      </radialGradient>
    </defs>
    <g clip-path="url(#cover-curve)">
      <rect x="60" y="80" width="527" height="472" fill="url(#keys-photo)" role="img" aria-label="Photo: a hand passing a set of house keys to a new owner, on a dark navy background"/>
      <rect x="60" y="551" width="527" height="191" fill="var(--yellow)"/>
      <rect x="60" y="742" width="527" height="30" fill="var(--red)"/>
    </g>
    <rect x="587" y="80" width="474" height="692" fill="url(#right-glow)"/>
    <rect x="587" y="80" width="474" height="33" fill="var(--yellow)"/>
    <rect x="587.5" y="80.5" width="473" height="691" fill="none" stroke="#2b3346" stroke-width="1"/>
  </svg>

  <section class="copy intro">
    <h2 class="title-light">Let me introduce myself</h2>
    <p>I'm originally from Chicago, but I'm a full-fledged California girl now. I've lived and worked in Orange County since 1996. I always say where we live is the next best thing to living on a tropical island. I've traveled to many and I'm always happy to come back to my Laguna Niguel home.</p>
    <p>My passion for this area is why I'm in Real Estate. I consider myself incredibly fortunate to sell homes and help people purchase homes in an area that I love with all my heart.</p>
    <p>This passion also carries over in representing my clients with the highest degree of professionalism, enthusiasm and care. My business is built on exceptional customer service and I'm grateful my clients are mostly repeat and referrals.</p>
  </section>

  <section class="copy tenet">
    <h2 class="title-light">My Core Tenet</h2>
    <p>It's All About YOU!</p>
    <p>My #1 priority is understanding YOUR needs and YOUR objectives. This understanding, along with working diligently on your behalf, means we accomplish your goal whether you're purchasing your 1st home or selling a home you've loved so you can move on to the next chapter of your life</p>
  </section>

  <section class="copy services">
    <h2>Real Estate Services &amp; Beyond…</h2>
    <p>Simply put, I help people who are local, relocating and investing, sell and purchase homes in Southern California. For purchases outside of California, I can refer to a network of agents across the country.</p>
    <p>I also provide a team who is dedicated to providing outstanding customer service throughout the transaction. My team includes a network of lenders, title, and escrow officers, in house CPA, stagers, photographers, contractors and more.</p>
  </section>

  <section class="copy selling">
    <h2 class="section-title">SELLING YOUR HOME</h2>
    <p>Selling your home is not like any other business transaction. It's also personal. My priority as your Listing Agent is to guide you through what can be a complicated and sometimes emotional process.</p>
    <p>I place great emphasis on marketing your property with professional photographs, along with harnessing the power of the Internet and the virtual world to reach as many buyers as possible. Your property will be marketed to the public as well as to other agents, thus creating maximum exposure of your home.</p>
    <p>When we first meet to discuss selling your home, it's essential for me to gain an understanding of your unique needs such as timelines, expectations and financial considerations, just to name a few. From there, I begin the process of listing and marketing your home. I lead you through negotiations and more paperwork than you ever care to do, guiding you to the successful closing of your home.</p>
  </section>

  <section class="copy buying">
    <h2 class="section-title">BUYING A HOME</h2>
    <p>If you're thinking about buying a home, it's imperative you have an accomplished, real estate professional by your side to walk you through what is likely the largest purchase of your life.</p>
    <p>To get started, I like to meet with you so we have an opportunity to get to know each other as purchasing a home is a uniquely, personal endeavor. At that time, we can discuss your goals and if it's a good time for you to purchase a home.</p>
    <p>From there, the first step is to obtain a pre-approval from a lender. I'm able to recommend various lenders who can introduce and explain the various loan products available.</p>
    <p>After you've been pre-approved, that's when the fun starts! I guide you through the home buying adventure every step of the way and look forward to handing you the keys to your new home.</p>
  </section>

  <section class="copy testimonials">
    <h2 class="section-title">TESTIMONIALS:</h2>
    <div class="testimonial-cols">
      <div>
        <p>Dana got us an amazing deal on our new home and sold our old home in a week. Dana is patient, hardworking, professional and most importantly HONEST. Dana is definitely one of the best in the business!</p>
        <p>Priya &amp; Adam Rowe</p>
        <p>Dana is the kind of Real Estate professional everyone wants to represent them. She is knowledgeable, ethical, energetic, and follows up on every detail. Her honesty, integrity and expertise combined make her a very special and remarkable professional. We were lucky to find her!</p>
        <p>Henry &amp; Kate Mercer</p>
      </div>
      <div>
        <p>During the home buying process, Dana becomes your trusted advisor, mentor and friend. Her knowledge of the industry, community and market are best in class. A true professional! Dana aligned her goals with my own and understood the motivation behind my purchase. Dana is unequivocally the reason why I was able to purchase my home in Laguna Niguel and provide my family with a world-class community. Without her guidance and experience, I would still be in the market attempting to navigate the ever-changing work of real estate.</p>
        <p>Yasmin Calder</p>
      </div>
    </div>
  </section>
</div>
</body>
</html>
```